High End Cosmetic Packaging Design Project

Looking for packaging for 2 products for a High end skin care line aimed at the 35+ year old women. Color scheme is Pantone 2765c with accents of metallic silver, copper or gold, Pantone colors 871-877c. Possible watermark in the background or a 3D image. We are open to any good ideas and suggestions. Box dimensions for the 2 products are small, approximately 4.375 inches high and 1.5 inches square. I have attached an image of the logo. I have the logo files in all the various forms. 1 box is for a Vitamin C Serum and the other box is for an Anti Aging Serum. Boxes are the same but the text will be different on both products. I will supply the text for the boxes later, including directions & ingredients and a UPC code that has to go on the underside of the box. It has to be an elegant design that will stand out in photos online. Good and quick communication & feedback between you and us is essential. I have attached a jpg of our new logo. I have this logo in all available forms
*****We are open to all ideas and want your ideas and input. The bottles that go inside these boxes are a deep violet almost black kovra glass. This is where the pantone color selection came from but upon further thought it may not be the right choice. We were out looking at cosmetic packaging today and thought also as an idea that a dark charcoal, or black box might work as well. We have seen boxes in those dark shades in glossy, matt and some with a sparkle finish. Embossed lettering may be a possibility as well. Copper letters may be an idea that works well also. These are just ideas rolling aroung in our heads but please give us your ideas*******
Reason: to give designers more time
This is for the 35+ year old woman.
Communication

```html
<!DOCTYPE html>
<html lang="en">
<head>
<meta charset="utf-8">
<title>Veluna Serum Packaging</title>
<link rel="stylesheet" href="https://fonts.googleapis.com/css2?family=Arimo:wght@400&display=swap">
<style>
  :root {
    --page-bg: #f4f4f5;
    --box-black: #231f20;
    --silver-light: #f2f2f4;
    --silver-mid: #b9b6bc;
    --silver-dark: #6f6a72;
    --type-white: #f1f1f1;
    --accent-blue: #2a8fd0;
    --accent-magenta: #c42c9e;
  }
  * { margin: 0; padding: 0; box-sizing: border-box; }
  html, body {
    width: 928px;
    height: 1200px;
    overflow: hidden;
    background: var(--page-bg);
  }
  .canvas {
    position: relative;
    width: 928px;
    height: 1200px;
  }
  .box-front {
    position: absolute;
    top: 116px;
    width: 328px;
    height: 951px;
    padding: 9px;
    background: linear-gradient(90deg, var(--silver-dark), var(--silver-light) 20%, var(--silver-mid) 50%, var(--silver-light) 80%, var(--silver-dark));
  }
  .box-front--anti-aging { left: 157px; }
  .box-front--vitamin-c { left: 548px; }
  .box-panel {
    position: relative;
    width: 100%;
    height: 100%;
    background: var(--box-black);
    font-family: "Arimo", sans-serif;
    color: var(--type-white);
  }
  .brand-name {
    position: absolute;
    left: 43px;
    top: 125px;
    height: 290px;
    writing-mode: vertical-rl;
    transform: rotate(180deg);
    font-size: 60px;
    font-weight: 400;
    letter-spacing: 4px;
    line-height: 1;
    text-align: center;
    color: var(--type-white);
  }
  .product-mark {
    position: absolute;
    left: 110px;
    top: 560px;
    width: 90px;
    height: 90px;
    border: 6px solid var(--accent-blue);
  }
  .box-front--vitamin-c .product-mark { border-color: var(--accent-magenta); }
  .product-label {
    position: absolute;
    left: 40px;
    right: 40px;
    top: 788px;
    text-align: center;
  }
  .product-name {
    font-size: 29px;
    letter-spacing: 0.5px;
    line-height: 1;
    padding-bottom: 10px;
    border-bottom: 2px solid var(--type-white);
  }
  .product-type {
    margin-top: 9px;
    font-size: 18px;
    letter-spacing: 1px;
    text-align: right;
    padding-right: 22px;
  }
</style>
</head>
<body>
<main class="canvas">
  <section class="box-front box-front--anti-aging">
    <div class="box-panel">
      <div class="brand-name">VELUNA</div>
      <div class="product-mark" aria-hidden="true"></div>
      <div class="product-label">
        <div class="product-name">ANTI AGING</div>
        <div class="product-type">SERUM</div>
      </div>
    </div>
  </section>

  <section class="box-front box-front--vitamin-c">
    <div class="box-panel">
      <div class="brand-name">VELUNA</div>
      <div class="product-mark" aria-hidden="true"></div>
      <div class="product-label">
        <div class="product-name">VITAMIN C</div>
        <div class="product-type">SERUM</div>
      </div>
    </div>
  </section>
</main>
</body>
</html>
```